Business cards design on a high standard

We advise clients on insurance and financial matters, since these clients pay for our advice, the design should have a high standard. Our logo should be included. From the colors we are open for everything.

Colors

Designer to choose colors to be used in the design.

```html
<!DOCTYPE html>
<html lang="en">
<head>
<meta charset="utf-8">
<title>Alpen Counsel – Business Cards</title>
<link href="https://fonts.googleapis.com/css2?family=Roboto:wght@400;700&display=swap" rel="stylesheet">
<style>
  :root {
    --stage: #2b2b2d;
    --card-white: #ffffff;
    --brand-red: #e01010;
    --ink: #2a2a2a;
    --ink-soft: #555555;
    --rule: #9a9a9a;
  }
  * { margin: 0; padding: 0; box-sizing: border-box; }
  html, body {
    width: 1200px; height: 1108px; overflow: hidden;
    background: var(--stage);
    font-family: "Roboto", Arial, sans-serif;
  }
  .stage { position: relative; width: 1200px; height: 1108px; }
  .card {
    position: absolute; top: 259px;
    width: 360px; height: 590px;
    border-radius: 26px;
  }
  .card--front { left: 180px; background: var(--card-white); }
  .card--back { left: 660px; background: var(--brand-red); }

  .front__brand {
    position: absolute; top: 150px; left: 0; right: 0;
    text-align: center; color: var(--brand-red);
    font-weight: 700; font-size: 40px; letter-spacing: 2px;
  }
  .front__person { position: absolute; top: 330px; left: 0; right: 0; text-align: center; }
  .person__name { color: var(--brand-red); font-weight: 700; font-size: 22px; letter-spacing: 0.5px; }
  .person__title { color: var(--ink); font-size: 17px; margin-top: 2px; }

  .icon-row {
    position: absolute; top: 400px; left: 40px; right: 40px;
    display: flex; align-items: center; gap: 8px;
  }
  .icon-row__rule { flex: 1; height: 1px; background: var(--rule); }
  .icon { width: 26px; height: 26px; border-radius: 4px; background: var(--brand-red); display: flex; align-items: center; justify-content: center; }

  .front__contact {
    position: absolute; top: 440px; left: 0; right: 0;
    text-align: center; color: var(--ink); font-size: 18px; line-height: 26px;
  }
  .front__divider { position: absolute; top: 522px; left: 70px; right: 70px; height: 1px; background: var(--rule); }
  .front__address {
    position: absolute; top: 532px; left: 0; right: 0;
    text-align: center; color: var(--ink); font-size: 18px; line-height: 24px;
  }

  .back__brand {
    position: absolute; top: 270px; left: 0; right: 0;
    text-align: center; color: var(--card-white);
    font-weight: 700; font-size: 40px; letter-spacing: 2px;
  }
</style>
</head>
<body>
<main class="stage">
  <section class="card card--front">
    <div class="front__brand">ALPEN COUNSEL</div>
    <div class="front__person">
      <div class="person__name">MARCUS KELLER</div>
      <div class="person__title">Managing Director</div>
    </div>
    <div class="icon-row">
      <span class="icon-row__rule"></span>
      <span class="icon" aria-label="Phone">
        <svg width="16" height="16" viewBox="0 0 24 24"><path fill="#fff" d="M6.6 10.8a15 15 0 0 0 6.6 6.6l2.2-2.2a1 1 0 0 1 1-.25 11.4 11.4 0 0 0 3.6.57 1 1 0 0 1 1 1V20a1 1 0 0 1-1 1A17 17 0 0 1 3 4a1 1 0 0 1 1-1h3.5a1 1 0 0 1 1 1c0 1.25.2 2.45.57 3.57a1 1 0 0 1-.25 1z"/></svg>
      </span>
      <span class="icon" aria-label="Email">
        <svg width="16" height="16" viewBox="0 0 24 24"><rect x="3" y="6" width="18" height="12" fill="none" stroke="#fff" stroke-width="2"/><path d="M3 6l9 7 9-7" fill="none" stroke="#fff" stroke-width="2"/></svg>
      </span>
      <span class="icon" aria-label="Website">
        <svg width="16" height="16" viewBox="0 0 24 24"><circle cx="12" cy="12" r="8" fill="none" stroke="#fff" stroke-width="2"/><path d="M4 12h16M12 4c3 3 3 13 0 16M12 4c-3 3-3 13 0 16" fill="none" stroke="#fff" stroke-width="1.5"/></svg>
      </span>
      <span class="icon-row__rule"></span>
    </div>
    <div class="front__contact">
      <div>041-987 654 321</div>
      <div>hello@alpencounsel.com</div>
      <div>www.alpencounsel.com</div>
    </div>
    <div class="front__divider"></div>
    <div class="front__address">
      <div>18, Linden Street here,</div>
      <div>40210,Northland</div>
    </div>
  </section>

  <section class="card card--back">
    <div class="back__brand">ALPEN</div>
  </section>
</main>
</body>
</html>
```